Tall Glass Web site design

The aim of Tall Glass is to provide an online service which allows customers to pre-order drinks and gain incentives such as fast entry, special offers (drinks, entry fees), as well as allowing customers to compare drinking establishments based upon costs and ratings.

what is required is the design of the pages stated below completed to the specifications.

Target Market(s)

The target market of Tall Glass is men and women between the ages of 18 to 26 mainly. Within the age range of 18 to 26 the more specific target groups

Industry/Entity Type

Online

Requirements
Must have
• What is required to be designed

Website to be viewable on different systems e.g desktop, laptop and for mobile devices a mobile friendly page

Home page

Logo
Company name
Log in
Sign up
Help
Social media links, Follow us link

Bar, pub, club search function
Search by postcode, establishment type, distance

Pictorial instructions of how to use the site like ( quick plate). The stages are 1) select location 2) build order and pay 3) pick up from bar

Pre load results of establishments

Drinking establishment sign up

Map showing search results

List of results

My basket window which shows your order

Pop out box for customer sign up

Buttons for FAQ, general information, company information, Privacy policy ect at bottom of page

The home page is required to be Clear, simple, easy to use and stylish but not over the top with to much information which will confuse the customers. The preloaded results need to be obvious and where can be seen. The pictorial instructions should go below the preloaded results. Once the search criteria has been filled in and has been submitted the preloaded results and pictorial instructions will be removed and be replaced by the map and search results.

Drinking establishment personal page requires

Details of drinking establishment (name, address, contact, map)
list of drinks avliable
My basket
Special Offers
Gallery
Calendar
Reviews section at the bottom

When a person clicks on a drinking establishment page what that person should see when they open the page is company name logo
with a list of the drinks they offer and special offers. Tabs or buttons for gallery, establishment details, calender and special offers should be located along top or down the left. when they are clicked on they will replace the menu.

The colour scheme is based around the logo which is attached. We do not want any pink or overly bright colours which would not go with the logo.

A site which we like is this one
http://www.quick-plate.example/
this site is perfect simple, clear but also good looking. If you need inspiration you should use this site as a starting point.
Should not have
• what should be avoided is a site which like this one http://famishedden.example/~beta/?gclid=QWERTYzxcvbnASDFghjkLMNOPq

it is to complicated with bad font and colours. The site just feels cheesy and not classy. we like very little about this site

```html
<!DOCTYPE html>
<html lang="en">
<head>
<meta charset="utf-8">
<title>Tall Glass – Order your round online</title>
<link href="https://fonts.googleapis.com/css2?family=Open+Sans:wght@400;600;700&family=Cabin+Sketch:wght@400;700&display=swap" rel="stylesheet">
<style>
  :root{
    --brand:#2e3192;
    --brand-dark:#1b1f8a;
    --brand-light:#5a5fd6;
    --text:#444444;
    --muted:#6b6b6b;
    --rule:#c58b2c;
    --paper:#ffffff;
    --section-grey:#ebebeb;
    --footer-muted:#a9abd9;
  }
  *{box-sizing:border-box;margin:0;padding:0}
  html,body{width:1187px;height:1200px;overflow:hidden}
  body{position:relative;background:#fff;font-family:"Open Sans",Arial,sans-serif;color:var(--text)}
  .abs{position:absolute}

  /* header */
  .brand{left:183px;top:20px;display:flex;align-items:center;gap:12px}
  .brand-dot{width:72px;height:72px;border-radius:50%;background:#b9b9b9}
  .brand-name{font-size:30px;font-weight:700;color:var(--brand);letter-spacing:.3px}
  .social{display:flex;gap:3px}
  .social span{width:23px;height:23px;border-radius:50%;background:var(--brand);display:block}
  .social--top{left:903px;top:24px}
  .cart{left:551px;top:59px;display:flex;align-items:center;font-size:12.5px;color:var(--muted);height:22px}
  .cart svg{margin-right:6px}
  .cart b{color:#2a5bd7;font-weight:700;margin-right:3px}
  .cart .sub{color:#2a5bd7;font-weight:700;margin-left:3px}
  .btn-checkout{margin-left:8px;width:72px;height:21px;border:1px solid #b5b5b5;background:linear-gradient(#ececec,#d4d4d4);font-size:12.5px;color:#444;display:flex;align-items:center;justify-content:center}
  .account{left:816px;top:60px;font-size:14.5px;font-weight:700;color:#555}
  .help{left:928px;top:59px;width:80px;height:23px;border:1px solid #c9c9c9;border-radius:4px;font-size:12px;color:var(--brand);display:flex;align-items:center;justify-content:center;background:#fff;box-shadow:1px 1px 2px rgba(0,0,0,.12)}

  /* search banner */
  .search-band{left:183px;top:125px;width:821px;height:134px}
  .search-title{left:234px;top:140px;font-family:"Cabin Sketch",cursive;font-weight:700;font-size:39px;color:#fff;letter-spacing:.5px}
  .field{top:200px;height:30px;background:#fff;border:1px solid #d5d5d5;font-family:Arial,sans-serif;font-size:14px;color:#666;display:flex;align-items:center;padding:0 9px;justify-content:space-between}
  .field .caret{width:0;height:0;border-left:4px solid transparent;border-right:4px solid transparent;border-top:5px solid #333}
  .btn-search{left:766px;top:200px;width:154px;height:31px;background:linear-gradient(#6a6fe0,#3d42bd);border:1px solid #8c90ee;box-shadow:0 2px 3px rgba(0,0,0,.35);color:#fff;font-weight:700;font-size:15.5px;display:flex;align-items:center;justify-content:center;gap:6px;letter-spacing:.2px}

  /* listings */
  .section-title{left:183px;top:280px;font-family:"Cabin Sketch",cursive;font-weight:700;font-size:40px;color:#4b4b4b}
  .venue{width:390px;display:flex;gap:10px}
  .venue-thumb{width:78px;height:78px;flex:none;border:1px solid #e0e0e0;box-shadow:1px 1px 3px rgba(0,0,0,.18)}
  .venue h3{font-size:14.5px;font-weight:700;color:var(--brand-dark);margin-top:0;line-height:18px}
  .venue p{font-size:12.4px;line-height:18.7px;margin-top:4px;color:var(--text)}
  .rule{height:0;border-top:1px dashed var(--rule);width:380px}

  /* how it works */
  .how{left:0;top:721px;width:1187px;height:362px;background:var(--section-grey)}
  .how-title{left:0;top:748px;width:1187px;text-align:center;font-family:"Cabin Sketch",cursive;font-weight:700;font-size:39px;color:var(--brand)}
  .step-label{font-family:"Cabin Sketch",cursive;font-size:20px;color:#4a4a4a;text-align:center;width:240px}
  .step-art{border-radius:6px}

  /* footer */
  .footer{left:0;top:1077px;width:1187px;height:123px}
  .foot-links{left:179px;top:1122px;font-size:12.5px;color:#fff}
  .foot-links span{margin:0 5px}
  .copyright{left:179px;top:1142px;font-size:12.5px;color:var(--footer-muted)}
  .social--foot{left:895px;top:1127px}
  .social--foot span{background:#fff;width:23px;height:23px;margin-right:2px}
</style>
</head>
<body>

<!-- header -->
<div class="abs brand">
  <span class="brand-dot"></span>
  <span class="brand-name">Tall Glass</span>
</div>
<div class="abs social social--top" aria-label="Follow us"><span></span><span></span><span></span><span></span></div>
<div class="abs cart">
  <svg width="14" height="12" viewBox="0 0 14 12"><path d="M0 1h2.5l2 7h7l2-5.5H4" fill="none" stroke="#555" stroke-width="1.6"/><circle cx="5.5" cy="10.5" r="1.3" fill="#555"/><circle cx="10.5" cy="10.5" r="1.3" fill="#555"/></svg>
  <b>0</b> items | Subtotal : <span class="sub">$0.0</span>
  <span class="btn-checkout">Checkout</span>
</div>
<div class="abs account">Log in . Sign up</div>
<div class="abs help">NEED HELP</div>

<!-- search -->
<svg class="abs search-band" viewBox="0 0 821 134" preserveAspectRatio="none">
  <path fill="#2e3192" d="M2 5 L40 2 L80 6 L130 1 L190 5 L240 2 L300 6 L360 1 L420 5 L480 2 L540 6 L600 2 L660 5 L720 1 L780 5 L819 3 L817 40 L821 80 L818 130 L770 127 L720 133 L660 128 L600 132 L540 128 L480 133 L420 128 L360 132 L300 128 L240 133 L180 128 L120 132 L60 128 L0 132 L3 90 L0 50 Z"/>
</svg>
<div class="abs search-title">Order your round online</div>
<div class="abs field" style="left:237px;width:154px">Your Postcode</div>
<div class="abs field" style="left:408px;width:162px">Establishment Type <span class="caret"></span></div>
<div class="abs field" style="left:586px;width:163px">Distance <span class="caret"></span></div>
<div class="abs btn-search">SEARCH NOW
  <svg width="17" height="17" viewBox="0 0 17 17"><circle cx="7" cy="7" r="5" fill="none" stroke="#fff" stroke-width="2.2"/><path d="M10.5 10.5 L15.5 15.5" stroke="#fff" stroke-width="2.6" stroke-linecap="round"/></svg>
</div>

<!-- listings -->
<div class="abs section-title">Drinking establishment</div>

<div class="abs venue" style="left:185px;top:343px">
  <div class="venue-thumb" role="img" aria-label="Photo of a yellow cocktail" style="background:linear-gradient(160deg,#fff 30%,#f4c020 55%,#fff 75%)"></div>
  <div><h3>Duis sed lectus sit amet</h3><p>Nulla cursus ligula nec neque porttitor faucibus vel mauris ligula consequat nunc, et porttitor tortor libero vitae ipsum</p></div>
</div>
<div class="abs venue" style="left:619px;top:343px">
  <div class="venue-thumb" role="img" aria-label="Photo of a red iced drink with lime" style="background:linear-gradient(180deg,#fff 15%,#f36a3a 45%,#e8262a 80%,#fff 95%)"></div>
  <div><h3>Morbi feugiat adipiscing</h3><p>Duis sed lectus sit amet neque viverra ornare blandit sem at ante mattis et mattis turpis</p></div>
</div>
<div class="abs rule" style="left:185px;top:443px"></div>
<div class="abs rule" style="left:618px;top:443px"></div>

<div class="abs venue" style="left:185px;top:463px">
  <div class="venue-thumb" role="img" aria-label="Photo of a dark red cocktail" style="background:linear-gradient(180deg,#fff 15%,#c0381c 35%,#fff 60%)"></div>
  <div><h3>Aenean ornar</h3><p>Morbi feugiat adipiscing nibh sit amet mollis eleifend dapibus nunc id dignissim</p></div>
</div>
<div class="abs venue" style="left:619px;top:463px">
  <div class="venue-thumb" role="img" aria-label="Photo of a red cocktail with lime" style="background:linear-gradient(180deg,#fff 15%,#e0203a 35%,#fff 60%)"></div>
  <div><h3>Nullam enim magna</h3><p>Proin porttitor tellus in lacus facilisis molestie commodo sem sed magna rutrum congue dapibus</p></div>
</div>
<div class="abs rule" style="left:185px;top:562px"></div>
<div class="abs rule" style="left:618px;top:562px"></div>

<div class="abs venue" style="left:185px;top:583px">
  <div class="venue-thumb" role="img" aria-label="Photo of an orange fruit drink" style="background:linear-gradient(180deg,#fff 10%,#f0501c 40%,#f08a1c 65%,#fff 90%)"></div>
  <div><h3>Vestibulum eu metus</h3><p>Nullam enim magna, laoreet ut laoreet eleifend venenatis vitae ultricies et, porta vel odio</p></div>
</div>
<div class="abs venue" style="left:619px;top:583px">
  <div class="venue-thumb" role="img" aria-label="Photo of apple juice beside an apple" style="background:linear-gradient(90deg,#fff 5%,#c8302a 30%,#f2b544 60%,#fff 95%)"></div>
  <div><h3>Etiam tempor sapien</h3><p>Phasellus pharetra arcu et est vulputate aliquet faucibus orci luctus et ultrices posuere cubilia</p></div>
</div>
<div class="abs rule" style="left:185px;top:682px"></div>
<div class="abs rule" style="left:618px;top:682px"></div>

<!-- how it works -->
<div class="abs how"></div>
<div class="abs how-title">How it Works</div>

<svg class="abs" style="left:0;top:810px" width="1187" height="230" viewBox="0 0 1187 230">
  <defs>
    <filter id="card-shadow" x="-10%" y="-10%" width="120%" height="130%">
      <feDropShadow dx="2" dy="6" stdDeviation="4" flood-color="#000" flood-opacity=".25"/>
    </filter>
  </defs>
  <g filter="url(#card-shadow)" fill="#fff">
    <path d="M199 26 L426 24 L434 212 L177 212 Z"/>
    <path d="M484 26 L711 24 L719 212 L462 212 Z"/>
    <path d="M769 26 L996 24 L1004 212 L747 212 Z"/>
  </g>
  <g fill="#d4d4d4">
    <rect x="264" y="10" width="97" height="24" transform="rotate(-1 312 22)"/>
    <rect x="549" y="10" width="97" height="24" transform="rotate(-1 597 22)"/>
    <rect x="834" y="10" width="97" height="24" transform="rotate(-1 882 22)"/>
  </g>
  <g fill="var(--brand)">
    <circle cx="219" cy="56" r="13"/>
    <circle cx="503" cy="56" r="13"/>
    <circle cx="789" cy="56" r="13"/>
  </g>
  <g fill="#fff" font-family="Open Sans, sans-serif" font-weight="700" font-size="16" text-anchor="middle">
    <text x="219" y="62">1</text><text x="503" y="62">2</text><text x="789" y="62">3</text>
  </g>
  <g fill="none" stroke="#777" stroke-width="1.5">
    <path d="M390 96 Q425 80 452 105"/><path d="M446 101 L453 107 L452 97"/>
    <path d="M672 96 Q707 80 740 105"/><path d="M734 101 L741 107 L740 97"/>
  </g>
</svg>

<div class="abs step-art" role="img" aria-label="Illustration of a folded map with a magnifying glass" style="left:246px;top:872px;width:150px;height:92px;background:linear-gradient(135deg,#5aa6d8,#6cb14a 55%,#9a6a3a)"></div>
<div class="abs step-art" role="img" aria-label="Illustration of a cash register printing a receipt" style="left:530px;top:862px;width:126px;height:100px;background:linear-gradient(180deg,#e8e8e8,#e6c25a 40%,#a9b8c8)"></div>
<div class="abs step-art" role="img" aria-label="Illustration of two glasses of red wine" style="left:826px;top:860px;width:100px;height:104px;background:linear-gradient(180deg,#eeeeee 10%,#8a1530 45%,#dcdcdc 80%)"></div>

<div class="abs step-label" style="left:186px;top:970px">Select Location</div>
<div class="abs step-label" style="left:471px;top:970px">build order and pay</div>
<div class="abs step-label" style="left:756px;top:970px">pick up from bar</div>

<!-- footer -->
<svg class="abs footer" viewBox="0 0 1187 123" preserveAspectRatio="none">
  <path fill="#2e3192" d="M0 6 L60 3 L120 7 L180 2 L240 6 L300 3 L360 7 L420 2 L480 6 L540 3 L600 7 L660 2 L720 6 L780 3 L840 7 L900 2 L960 6 L1020 3 L1080 7 L1140 2 L1187 5 L1187 123 L0 123 Z"/>
</svg>
<div class="abs foot-links">FAQ<span>|</span>general information<span>|</span>company information<span>|</span>Privacy policy</div>
<div class="abs copyright">Copyright © 2013 Tall Glass. All rights reserved</div>
<div class="abs social social--foot" aria-label="Follow us"><span></span><span></span><span></span><span></span></div>

</body>
</html>
```